Banner Ad for website hompage - Design Project

We need 4 banner ads for the homepage of a Rent a Car company based in dubai. We rent a wide range of cars but mainly deal in the affordable cars category. Our website colors are mainly red, white and black and I can send pictures of the website (attached) if you want something to compare possible design ideas with. The banners need to promote different messages and must be appealing to the end user. It must also use pictures of cars that exist in our fleet (Pls note: this is only if you are using cars in the banner ad)

The 4 banner ads needed are as follows:
1) should promote something along the lines of we have 20+ models available and reserve a car now (This banner should also have a reserve now button, not the actual button but it's design. The button will be made and coded by us)
2) should promote something along the lines of we offer personalised service and we look after each and every custoemr individually
3) we provide attractive rates based on daily, weekly, monthly and longer rental periods (should also incorporate a reserve now message)
4) Like us on bramblex and follow us on social media for additional offers and discounts (would like for this to have a like button design implemented in it which will be linked to bramblex.)

Also please not the picture file size is 940pixels by 400pixels

Finally: I also need the psd files for the banners.

Reason: giving people more time for revisions

It Company

```html
<!DOCTYPE html>
<html lang="en">
<head>
<meta charset="utf-8">
<title>Keystone rent a car</title>
<link rel="stylesheet" href="https://fonts.googleapis.com/css2?family=Open+Sans:wght@400;600;700;800&display=swap">
<style>
:root{
  --brand-red:#e2391b;
  --banner-red:#e63a10;
  --nav-grey:#444444;
  --ink:#000000;
  --paper:#ffffff;
  --header-top:#ffffff;
  --header-bottom:#ececec;
}
*{margin:0;padding:0;box-sizing:border-box}
html,body{width:1200px;height:559px;overflow:hidden;background:var(--paper);font-family:"Open Sans",sans-serif}
.page{position:relative;width:1200px;height:559px}
.site-header{position:absolute;left:0;top:0;width:1200px;height:116px;background:linear-gradient(var(--header-top),var(--header-bottom));border-bottom:1px solid #dcdcdc}
.brand{position:absolute;left:153px;top:30px;color:var(--brand-red);font-weight:700;font-size:34px;line-height:1;letter-spacing:-0.5px}
.brand small{display:block;font-size:19px;margin-top:4px;margin-left:30px}
.main-nav{position:absolute;left:429px;top:56px;display:flex;gap:21px}
.main-nav a{color:var(--nav-grey);text-decoration:none;font-weight:700;font-size:15.5px;letter-spacing:-0.3px;padding-bottom:1px}
.main-nav a.is-active{color:var(--brand-red);border-bottom:2px solid var(--brand-red)}
.hero{position:absolute;left:0;top:116px;width:1200px;height:394px;overflow:hidden;background:var(--banner-red)}
.hero-photo{position:absolute;left:0;top:0}
.tag{position:absolute;left:155px;top:85px;background:var(--ink);color:var(--paper);font-weight:700;font-size:18px;padding:7px 13px 9px;line-height:1.2}
.tag::after{content:"";position:absolute;left:0;bottom:-12px;border-top:12px solid var(--ink);border-right:12px solid transparent}
.headline{position:absolute;left:153px;top:128px;color:var(--paper);font-weight:700;font-size:83px;line-height:1;letter-spacing:-4px}
.headline sup{font-size:42px;vertical-align:top;position:relative;top:4px;letter-spacing:0;margin-right:8px}
.subline{position:absolute;left:155px;top:208px;color:var(--paper);font-weight:700;font-size:27px;letter-spacing:-1.3px;line-height:1.2}
.reserve{position:absolute;left:155px;top:267px;width:258px;height:58px;background:var(--ink);border:3px solid var(--paper);border-radius:29px;color:var(--paper);font-size:21px;padding-left:74px;line-height:52px}
.reserve .avatar{position:absolute;left:-3px;top:-4px;width:60px;height:60px;border-radius:50%;background:radial-gradient(circle,#ffffff,#d9d9d9);border:2px solid var(--paper)}
.prev{position:absolute;left:110px;top:187px}
.pager{position:absolute;left:518px;top:287px}
.hero-shadow{position:absolute;left:100px;top:506px;width:1000px;height:28px;background:radial-gradient(ellipse at center top,rgba(0,0,0,.28),rgba(0,0,0,0) 70%)}
</style>
</head>
<body>
<div class="page">
  <header class="site-header">
    <div class="brand">Keystone<small>rent a car</small></div>
    <nav class="main-nav">
      <a href="#">HOME</a>
      <a href="#" class="is-active">ABOUT US</a>
      <a href="#">SERVICES &amp; BENEFITS</a>
      <a href="#">BLOG</a>
      <a href="#">CONTACT US</a>
      <a href="#">RESOURCES</a>
    </nav>
  </header>

  <section class="hero">
    <svg class="hero-photo" width="1200" height="394" viewBox="0 0 1200 394" role="img" aria-label="Red sedan driving on a coastal mountain road under blue sky">
      <defs>
        <linearGradient id="photoTone" x1="0" y1="0" x2="0" y2="1">
          <stop offset="0" stop-color="#b9d3e8"/>
          <stop offset=".35" stop-color="#c7a99a"/>
          <stop offset=".6" stop-color="#b0232a"/>
          <stop offset="1" stop-color="#8c8c8e"/>
        </linearGradient>
      </defs>
      <polygon points="692,0 1200,0 1200,394 506,394" fill="url(#photoTone)"/>
      <line x1="692" y1="0" x2="506" y2="394" stroke="#ffffff" stroke-width="2"/>
    </svg>

    <svg class="prev" width="36" height="44" viewBox="0 0 36 44" aria-hidden="true">
      <circle cx="17" cy="22" r="16" fill="none" stroke="rgba(255,255,255,.5)" stroke-width="2"/>
      <polyline points="20,14 13,22 20,30" fill="none" stroke="rgba(255,255,255,.6)" stroke-width="3"/>
    </svg>

    <div class="tag">we have over</div>
    <div class="headline">20<sup>+</sup>Models</div>
    <div class="subline">available and reserve a car now</div>
    <div class="reserve"><span class="avatar" role="img" aria-label="Service agent holding car keys"></span>RESERVE NOW</div>

    <svg class="pager" width="62" height="26" viewBox="0 0 62 26" aria-hidden="true">
      <polygon points="10,0 62,0 54,24 0,24" fill="#ffffff"/>
      <circle cx="14" cy="12" r="4" fill="#000"/>
      <circle cx="24" cy="12" r="4" fill="#c0200a"/>
      <circle cx="34" cy="12" r="4" fill="#c0200a"/>
      <circle cx="44" cy="12" r="4" fill="#c0200a"/>
    </svg>
  </section>
  <div class="hero-shadow"></div>
</div>
</body>
</html>
```